Option Sheet

We need a one page option sheet with a left to right reading of the five options. It should be a one sheet, multiple colors and definitive separations between options This is used in a sales consultation. Backround or colors not in option need to have the follow RGB value (5 red, 20 green, 63 blue)

We added a smaller text file, please change that point

Target Market(s)

Divorce

Industry/Entity Type

Legal

Requirements
Must have
• 1) All five options left to right
• 2)language included in sheet

```html
<!DOCTYPE html>
<html lang="en">
<head>
<meta charset="utf-8">
<title>Five Options – Divorce</title>
<link href="https://fonts.googleapis.com/css2?family=Montserrat:wght@500;700&family=Source+Sans+3:ital,wght@0,400;0,700;1,300&display=swap" rel="stylesheet">
<style>
  :root {
    --navy: rgb(5, 20, 63);
    --white: #ffffff;
    --ink: #3a3a3a;
    --ink-soft: #555a63;
    --rule: #e3e5ea;
    --divider: #cfd2d8;
    --opt-1: #f4532c;
    --opt-2: #d94fa2;
    --opt-3: #4a3796;
    --opt-4: #8dc63f;
    --opt-5: #0e9a48;
  }
  * { box-sizing: border-box; margin: 0; padding: 0; }
  html, body { width: 1200px; height: 680px; overflow: hidden; }
  body { background: var(--navy); position: relative; font-family: "Source Sans 3", sans-serif; }

  .sheet-title { position: absolute; top: 28px; left: 0; width: 1200px; text-align: center; color: var(--white); font-family: "Montserrat", sans-serif; }
  .sheet-title .kicker { display: block; font-weight: 500; font-size: 29px; line-height: 34px; letter-spacing: 0.5px; }
  .sheet-title .topic { display: block; font-weight: 700; font-size: 62px; line-height: 68px; letter-spacing: 1px; margin-top: 4px; }

  .options { position: absolute; left: 16px; top: 158px; width: 1169px; height: 505px; background: var(--white); border-radius: 6px; display: flex; }

  .option { position: relative; width: 233.8px; height: 100%; }
  .option + .option::before { content: ""; position: absolute; left: 0; top: 18px; bottom: 28px; width: 1px; background: var(--divider); }

  .option-label { position: absolute; top: 15px; left: 0; width: 100%; text-align: center; font-style: italic; font-weight: 300; font-size: 13.5px; line-height: 16px; color: var(--ink-soft); }
  .option-name { position: absolute; top: 31px; left: 0; width: 100%; text-align: center; font-weight: 700; font-size: 29px; line-height: 36px; letter-spacing: -0.6px; color: var(--accent); }
  .option--two-line .option-label { top: 5px; }
  .option--two-line .option-name { top: 21px; line-height: 23px; }

  .option-rule { position: absolute; top: 80px; left: 6px; right: 6px; height: 1px; background: linear-gradient(90deg, transparent, var(--accent) 20%, var(--accent) 80%, transparent); }

  .group-title { position: absolute; left: 20px; font-size: 18px; line-height: 22px; font-weight: 400; color: var(--ink); }
  .group-split { position: absolute; left: 20px; right: 20px; height: 1px; background: linear-gradient(90deg, transparent, var(--rule) 15%, var(--rule) 85%, transparent); }

  .points { position: absolute; left: 0; width: 100%; list-style: none; }
  .points li { position: relative; padding-left: 47px; padding-right: 8px; font-style: italic; font-weight: 300; font-size: 14.6px; line-height: 15px; color: var(--ink-soft); margin-bottom: 15px; letter-spacing: -0.2px; }
  .points li::before { content: ""; position: absolute; left: 24px; top: 3px; width: 9.6px; height: 9.6px; border-radius: 50%; background: var(--accent); }

  .adv-title { top: 105px; }
  .adv-list { top: 136px; }
  .split { top: 206px; }
  .dis-title { top: 227px; }
  .dis-list { top: 258px; }
  .option--long-adv .split { top: 325px; }
  .option--long-adv .dis-title { top: 346px; }
  .option--long-adv .dis-list { top: 378px; }

  .option--nothing { --accent: var(--opt-1); }
  .option--counseling { --accent: var(--opt-2); }
  .option--diy { --accent: var(--opt-3); }
  .option--limited { --accent: var(--opt-4); }
  .option--hire { --accent: var(--opt-5); }
</style>
</head>
<body>
  <header class="sheet-title">
    <span class="kicker">Five Options</span>
    <span class="topic">DIVORCE</span>
  </header>

  <main class="options">
    <section class="option option--nothing">
      <p class="option-label">option #1</p>
      <h2 class="option-name">Do Nothing</h2>
      <div class="option-rule"></div>
      <h3 class="group-title adv-title">Advantages:</h3>
      <ul class="points adv-list">
        <li>Stay married</li>
        <li>No life Changes</li>
      </ul>
      <div class="group-split split"></div>
      <h3 class="group-title dis-title">Disadvantages:</h3>
      <ul class="points dis-list">
        <li>Remain unhappy, depressed, anxious</li>
        <li>Money and assets may disappear</li>
        <li>What is going to change?</li>
      </ul>
    </section>

    <section class="option option--counseling">
      <p class="option-label">option #2</p>
      <h2 class="option-name">Go to Counseling</h2>
      <div class="option-rule"></div>
      <h3 class="group-title adv-title">Advantages:</h3>
      <ul class="points adv-list">
        <li>Reconcile marriage</li>
        <li>Help make a better life</li>
      </ul>
      <div class="group-split split"></div>
      <h3 class="group-title dis-title">Disadvantages:</h3>
      <ul class="points dis-list">
        <li>Past issues are highlighted and may drudge up old wounds</li>
        <li>It may just clarify the reasons you need to separate and/or divorce</li>
        <li>Both parties must be invested and willing to participate</li>
      </ul>
    </section>

    <section class="option option--diy">
      <p class="option-label">option #3</p>
      <h2 class="option-name">Do it Yourself</h2>
      <div class="option-rule"></div>
      <h3 class="group-title adv-title">Advantages:</h3>
      <ul class="points adv-list">
        <li>No attorney fees</li>
        <li>You are your own attorney</li>
      </ul>
      <div class="group-split split"></div>
      <h3 class="group-title dis-title">Disadvantages:</h3>
      <ul class="points dis-list">
        <li>People often find that what is “fair,” may in fact, not be truly fair</li>
        <li>Often times, people do not know the risks</li>
        <li>Complicated legal system within intrigue rules</li>
        <li>Unsure how to complete the necessary paperwork and meet the deadlines</li>
      </ul>
    </section>

    <section class="option option--limited option--two-line">
      <p class="option-label">option #4</p>
      <h2 class="option-name">Limited<br>Representation</h2>
      <div class="option-rule"></div>
      <h3 class="group-title adv-title">Advantages:</h3>
      <ul class="points adv-list">
        <li>Balance between going alone and our limited involvement in the case</li>
      </ul>
      <div class="group-split split"></div>
      <h3 class="group-title dis-title">Disadvantages:</h3>
      <ul class="points dis-list">
        <li>Our terms may not benefit from our legal knowledge</li>
        <li>The legal consequences of your legal documents will not be explained to you so that you can formulate a plan for handling the rest of your case.</li>
        <li>Your spouse or other parties may cause your legal fees to increase significantly without action on your part</li>
      </ul>
    </section>

    <section class="option option--hire option--long-adv">
      <p class="option-label">option #5</p>
      <h2 class="option-name">Hire Us</h2>
      <div class="option-rule"></div>
      <h3 class="group-title adv-title">Advantages:</h3>
      <ul class="points adv-list">
        <li>Gain the full benefits of our experience</li>
        <li>Have a team of Family Law focus attorneys</li>
        <li>Often saves you or makes you money in the long run</li>
        <li>Save you time, energy and stress</li>
      </ul>
      <div class="group-split split"></div>
      <h3 class="group-title dis-title">Disadvantages:</h3>
      <ul class="points dis-list">
        <li>Remain unhappy, depressed, anxious</li>
        <li>Money and assets may disappear</li>
        <li>What is going to change?</li>
      </ul>
    </section>
  </main>
</body>
</html>
```